Business Card for Marriage Commissioner

I am a marriage commissioner in the province of Alberta, meaning that I perform civil unions here. I have been trying to think of a unique design for my business card, something a bit different. A lot of "unique" designs seem to incorporate unique cuts or "some assembly required" or printed on plastic or meat. I would like my design to be a full colour card that is a typical business card size.

The information on the card should have:
Lou Varnik
my occupation: Marriage Commissioner
my website: www.louvarnik.ca
my e-mail: lou@louvarnik.ca
my phone: 780-418-2964

I originally submitted a design to the printer that had a screen capture of a findly search window, with my name and occupation in the text box. And underneath that, my phone number. Nothing else. They indicated they could not print this because it was a copyright violation.

One option on the design is I am a retired chemist-so a chemistry themed card would also be of interest, as long as it isn't a "Rusted Tide" theme, as I have that on my other business cards already...

I would prefer a single sided card, but I am open to a double sided card if it is clever!

I would also prefer not to have pictures of male and female couples as in my position I will also marry same sex couples. Same thing for male/female symbols. Someone has submitted two graduated cylinders in love, which is very clever, and gets around this male/female type.

Thanks for your help and interest.

Target Market(s)

Young couples.

Industry/Entity Type

Plastic

Requirements
Nice to have
• chemistry ideas!
Should not have
• Male/female pictures, male/female symbols.
No QR codes.
No transparent designs, will go on paper stock.

```html
<!DOCTYPE html>
<html lang="en">
<head>
<meta charset="utf-8">
<title>Lou Varnik – Alberta Marriage Commissioner</title>
<link rel="stylesheet" href="https://fonts.googleapis.com/css2?family=Yellowtail&family=Open+Sans:wght@400;600;700&display=swap">
<style>
  :root {
    --backdrop: #e9e6e2;
    --card: #ffffff;
    --teal: #2bb3b1;
    --rose: #e07a86;
    --rose-soft: #f2c1c6;
    --ink: #3a3a3a;
    --white: #ffffff;
  }
  html, body {
    margin: 0;
    width: 1200px;
    height: 1023px;
    overflow: hidden;
    background: var(--backdrop);
  }
  .business-card {
    position: absolute;
    left: 100px;
    top: 226px;
    width: 1000px;
    height: 571px;
    background: var(--card);
    border-radius: 6px;
    box-shadow: 0 12px 40px rgba(0,0,0,0.18);
    overflow: hidden;
    font-family: "Open Sans", Arial, sans-serif;
  }
  .identity {
    position: absolute;
    left: 60px;
    top: 30px;
  }
  .identity-name {
    margin: 0;
    font-family: "Yellowtail", "Brush Script MT", cursive;
    font-weight: 400;
    font-size: 96px;
    line-height: 1;
    color: var(--teal);
  }
  .identity-role {
    margin: 4px 0 0 14px;
    font-size: 24px;
    font-weight: 600;
    color: var(--ink);
    letter-spacing: 0.5px;
  }
  .love-tubes-art {
    position: absolute;
    left: 40px;
    top: 180px;
    width: 570px;
    height: 225px;
    border-radius: 8px;
    background: linear-gradient(120deg, #ffffff 0%, var(--rose-soft) 45%, var(--rose) 70%, #f7f7f7 100%);
  }
  .contact {
    position: absolute;
    left: 650px;
    top: 230px;
    margin: 0;
    padding: 0;
    list-style: none;
    font-size: 26px;
    color: var(--ink);
    line-height: 1.6;
  }
  .footer-band {
    position: absolute;
    left: 0;
    bottom: 0;
    width: 1000px;
    height: 150px;
  }
  .website {
    position: absolute;
    right: 60px;
    bottom: 32px;
    margin: 0;
    font-size: 32px;
    line-height: 1.2;
    font-weight: 700;
    letter-spacing: 4px;
    color: var(--white);
  }
</style>
</head>
<body>
  <section class="business-card">
    <header class="identity">
      <h1 class="identity-name">Lou Varnik</h1>
      <p class="identity-role">Alberta Marriage Commissioner</p>
    </header>

    <div class="love-tubes-art" role="img" aria-label="Illustration of two laboratory syringes joined by pink tubing that loops into the word love"></div>

    <ul class="contact">
      <li class="contact-phone">780-418-2964</li>
      <li class="contact-email">lou@louvarnik.ca</li>
    </ul>

    <svg class="footer-band" viewBox="0 0 1000 150" aria-hidden="true">
      <path d="M0 4 Q 420 94 1000 30 L1000 150 L0 150 Z" fill="var(--rose)"/>
      <path d="M0 4 Q 420 94 1000 30" fill="none" stroke="var(--teal)" stroke-width="8"/>
    </svg>
    <p class="website">www.louvarnik.ca</p>
  </section>
</body>
</html>
```